Etiketten-Design für Kräuterbonbon-Metalldose
Marlene Vosk hat sehr viel Talent. Das Design ist absolut kreativ.
Zielgruppe
Unsere Firma VelbraCor verkauft verschiedene Sorten Kräuterbonbons.
Wir brauchen ein Etikett, dass auf eine Metall-Dose (Durchmesser 10 cam, Höhe ca. 3 cm) geklebt wird.
Zielgruppe: jung-alt
Aufgabenstellung
Der Name unserer Kräuterbonbons ist Pfeffling.
Wir möchten, dass unsere Kunden, wenn sie das Etikett sehen einen Bezug zur Schweiz herstellen können.
Wir verwenden für unsere Bonbons unterschiedliche Kräuter für verschiedene Anwendungen:
Konkret sind erstmal 4 Dosen geplant:
-Kräutermischung aus 16 Kräuter gegen Husten
-Salbei gegen Halsschmerzen
-Anis gegen Magenschmerzen
-Zitrone/Ingwer für die Nerven
Vorderseite: Produktbeschreibung
Rückseite: unsere Herstellerangaben
Größenangaben der Dose: Durchmesser 10 cm, Höhe ca. 3 cm
Im Anhang habe ich Ihnen noch weitere/ genauere Informationen zur Verfügung bereitgestellt!

```html
<!DOCTYPE html>
<html lang="de">
<head>
<meta charset="utf-8">
<title>Nährwertetikett – Pfeffling Kräuterbonbons</title>
<link rel="stylesheet" href="https://fonts.googleapis.com/css2?family=Source+Sans+3:wght@400;600;700&display=swap">
<style>
  :root {
    --label-green: #6f7733;
    --white: #ffffff;
    --pattern-light: #f1f2ee;
    --pattern-mid: #e3e7df;
    --pattern-warm: #f4ead6;
  }
  * { margin: 0; padding: 0; box-sizing: border-box; }
  html, body {
    width: 1199px;
    height: 1200px;
    overflow: hidden;
    background: var(--white);
    font-family: "Source Sans 3", "Myriad Pro", sans-serif;
  }
  .canvas { position: relative; width: 1199px; height: 1200px; }

  .leaf-ring {
    position: absolute;
    left: 44px; top: 45px;
    width: 1110px; height: 1110px;
    border-radius: 50%;
    background: radial-gradient(circle at 70% 30%, var(--pattern-warm) 0%, var(--pattern-light) 40%, var(--pattern-mid) 100%);
  }
  .label-disc {
    position: absolute;
    left: 82px; top: 73px;
    width: 1036px; height: 1036px;
    border-radius: 50%;
    background: var(--label-green);
  }
  .sprig-ornament {
    position: absolute;
    left: 568px; top: 165px;
    width: 64px; height: 118px;
    border-radius: 32px;
    background: var(--white);
    opacity: 0.9;
  }
  .title {
    position: absolute;
    left: 0; right: 0; top: 316px;
    text-align: center;
    color: var(--white);
    font-weight: 700;
    font-size: 40px;
    letter-spacing: 0.2px;
  }
  .badge {
    position: absolute;
    top: 418px;
    width: 136px; height: 136px;
    border-radius: 50%;
    border: 5px solid var(--white);
    display: flex; align-items: center; justify-content: center;
  }
  .badge-core {
    width: 114px; height: 114px;
    border-radius: 50%;
    background: var(--white);
    color: var(--label-green);
    display: flex; flex-direction: column; align-items: center; justify-content: center;
    line-height: 1.25;
  }
  .badge-label { font-size: 16px; font-weight: 400; margin-bottom: 8px; }
  .badge-value { font-size: 20px; font-weight: 700; }
  .badge--kcal { left: 252px; }
  .badge--kj { left: 532px; }
  .badge--fat { left: 806px; }

  .nutrition-table {
    position: absolute;
    left: 251px; top: 613px;
    width: 699px; height: 256px;
    border: 3px solid var(--white);
    border-radius: 46px;
    padding: 22px 0 0 31px;
    color: var(--white);
    font-size: 23px;
    border-collapse: separate;
  }
  .nutrition-row { display: flex; height: 30.7px; align-items: center; }
  .nutrient { width: 419px; font-weight: 400; }
  .amount { font-weight: 700; }

  .laurel-ornament {
    position: absolute;
    left: 452px; top: 978px;
    width: 296px; height: 60px;
    border-radius: 30px;
    background: var(--white);
    opacity: 0.9;
  }
</style>
</head>
<body>
<div class="canvas">
  <div class="leaf-ring" role="img" aria-label="Umlaufendes Muster aus blassen Blättern in Grau, Grün und Beige"></div>
  <div class="label-disc"></div>
  <div class="sprig-ornament" role="img" aria-label="Kleines weißes Kräuterzweig-Ornament"></div>

  <h1 class="title">Unzubereitet für 100 Gramm</h1>

  <div class="badge badge--kcal">
    <div class="badge-core"><span class="badge-label">Energie</span><span class="badge-value">400 Kcal</span></div>
  </div>
  <div class="badge badge--kj">
    <div class="badge-core"><span class="badge-label">Energie</span><span class="badge-value">1670 kj</span></div>
  </div>
  <div class="badge badge--fat">
    <div class="badge-core"><span class="badge-label">Fett</span><span class="badge-value">0 g</span></div>
  </div>

  <div class="nutrition-table">
    <div class="nutrition-row"><span class="nutrient">Energie</span><span class="amount">400 Kcal &nbsp;/ 1670 kj</span></div>
    <div class="nutrition-row"><span class="nutrient">Fett</span><span class="amount">0 g</span></div>
    <div class="nutrition-row"><span class="nutrient">davon gesättigte Fettsäuren</span><span class="amount">0 g</span></div>
    <div class="nutrition-row"><span class="nutrient">kohlenhydrate</span><span class="amount">98 g</span></div>
    <div class="nutrition-row"><span class="nutrient">davon Zucker</span><span class="amount">76 g</span></div>
    <div class="nutrition-row"><span class="nutrient">Eiweiß</span><span class="amount">0 g</span></div>
    <div class="nutrition-row"><span class="nutrient">Salz</span><span class="amount">0 g</span></div>
  </div>

  <div class="laurel-ornament" role="img" aria-label="Weißes Lorbeerzweig-Ornament"></div>
</div>
</body>
</html>
```